Business Card

Can you please copy the format provided for the business cards.
Can the logo be in the colours of the last file as specified.

Can the text please be in grey

• Navy Blue: #00457C
• Grey Text: #555555
• Orange Text: #FDBF29

The names on the business card will be

Dorian Pike
0455 718 302
dorian.pike@tallowridgeleasing.example.au

Lvl 7, 14 Harlow Pde
Merrivale QLD 4388
PO Box 3412
Sunhaven MC QLD 9812
P: 1300 742 619
F: 1300 742 638
www.tallowridgeleasing.example.au

And

Leon Whitcombe
0467 590 148
leon.whitcombe@tallowridgeleasing.example.au

Lvl 7, 14 Harlow Pde
Merrivale QLD 4388
PO Box 3412
Sunhaven MC QLD 9812
P: 1300 742 619
F: 1300 743 905

```html
<!DOCTYPE html>
<html lang="en">
<head>
<meta charset="utf-8">
<title>Tallow Ridge Leasing – Business Card</title>
<link rel="stylesheet" href="https://fonts.googleapis.com/css2?family=Source+Sans+3:wght@400;600;700&display=swap">
<style>
  :root {
    --navy: #00457C;
    --grey-text: #555555;
    --orange: #FDBF29;
    --backdrop: #918d8c;
    --card: #ffffff;
  }
  * { margin: 0; padding: 0; box-sizing: border-box; }
  html, body {
    width: 1200px; height: 1200px; overflow: hidden;
    background: var(--backdrop);
    font-family: "Source Sans 3", sans-serif;
    color: var(--grey-text);
  }
  .card {
    position: absolute;
    left: 274px;
    width: 640px;
    height: 368px;
    background: var(--card);
    border-radius: 26px;
  }
  .card--front { top: 116px; }
  .card--back { top: 605px; }

  /* Front */
  .holder {
    position: absolute; top: 166px; left: 0; right: 0;
    text-align: center;
  }
  .card--front .holder { top: 50px; }
  .holder__name { font-size: 23px; font-weight: 700; line-height: 30px; }
  .holder__contact {
    margin-top: 14px;
    font-size: 18px; line-height: 23px; font-weight: 400;
  }
  .rule--horizontal {
    position: absolute; top: 182px; left: 138px;
    width: 351px; height: 4px; background: var(--orange);
  }
  .brand {
    position: absolute; display: flex; align-items: center;
  }
  .brand__mark { display: block; background: var(--navy); flex: none; }
  .brand__name {
    color: var(--navy); font-weight: 700; white-space: nowrap;
    letter-spacing: 0.2px;
  }
  .brand--front { top: 236px; left: 0; right: 0; justify-content: center; gap: 18px; }
  .brand--front .brand__mark { width: 58px; height: 58px; }
  .brand--front .brand__name { font-size: 28px; }

  /* Back */
  .address {
    position: absolute; top: 107px; left: 37px;
    font-size: 18px; line-height: 24px;
    list-style: none;
  }
  .rule--vertical {
    position: absolute; top: 83px; left: 262px;
    width: 4px; height: 202px; background: var(--orange);
  }
  .brand--back { top: 166px; left: 284px; gap: 16px; }
  .brand--back .brand__name { font-size: 22px; }
  .brand--back .brand__mark { width: 70px; height: 70px; }
  .website {
    position: absolute; top: 306px; left: 0; right: 0;
    text-align: center; font-size: 18px; font-weight: 600;
  }
</style>
</head>
<body>
  <section class="card card--front" aria-label="Business card front">
    <div class="holder">
      <p class="holder__name">Dorian Pike</p>
      <p class="holder__contact">0455 718 302<br>dorian.pike@tallowridge<br>leasing.example.au</p>
    </div>
    <div class="rule--horizontal"></div>
    <div class="brand brand--front">
      <span class="brand__mark"></span>
      <span class="brand__name">TALLOW RIDGE LEASING</span>
    </div>
  </section>

  <section class="card card--back" aria-label="Business card back">
    <ul class="address">
      <li>Lvl 7, 14 Harlow Pde</li>
      <li>Merrivale QLD 4388</li>
      <li>PO Box 3412</li>
      <li>Sunhaven MC QLD 9812</li>
      <li>P: 1300 742 619</li>
      <li>F: 1300 742 638</li>
    </ul>
    <div class="rule--vertical"></div>
    <div class="brand brand--back">
      <span class="brand__name">TALLOW RIDGE LEASING</span>
      <span class="brand__mark"></span>
    </div>
    <p class="website">www.tallowridgeleasing.example.au</p>
  </section>
</body>
</html>
```